Plant Grower/Nursery needs a fun, professional and fresh 1/2 page print ad for a high profile gar...

We need a print ad for a garden tour geared towards plant enthusiasts that support California Native, natural and sustainable plants. A good percentage of our target market want a conservation and earth friendly approach to gardens/landscaping. We want to target this market, as well as, people who are looking for a pretty/colorful landscape that require little water/maintenance. **PLEASE LET US KNOW IF YOU HAVE QUESTIONS OR NEED MORE INFORMATION. WE ALSO HAVE MANY MORE PICTURES IF THESE DON'T WORK FOR YOUR DESIGN. ***THE AD CAN HAVE AS FEW AS 1 PHOTO - WE ARE POSTING SEVERAL IN HOPES THAT YOU CAN FIND WHAT IS PERFECT FOR YOUR IDEA!!Thank you

Target Market(s)

Gardeners, Landscapers, Landscape Designers/Architects, Cities and Municipalities.

Industry/Entity Type

Agriculture

Font styles to use
Serif
Sans Serif

Colors

Requirements
Must have
• We believe in growing regionally appropriate plants for Southern California that beatify our natural and urban landscapes.
• For over 20 years, our owners and staff take pride in providing timely, expert, and honest service.
Nice to have
• At least 1 photo. Eye catchy with a modern earthy feel.
• Hundreds of species/hybrids in stock of California Natives, Succulents, Ornamental Grasses, Standard Stock Items and Unique Plants.

```html
<!DOCTYPE html>
<html lang="en">
<head>
<meta charset="utf-8">
<title>Native Plants Print Ad</title>
<link rel="stylesheet" href="https://fonts.googleapis.com/css2?family=Ubuntu:wght@400;500;700&display=swap">
<style>
  :root {
    --backdrop: #e2e2e2;
    --leaf-pale: #c9dcb4;
    --leaf-mid: #9cc48a;
    --leaf-deep: #5f9a55;
    --leaf-edge: #b8344f;
    --band-green: rgba(46, 125, 79, 0.92);
    --brand-green: #2d6b3a;
    --white: #ffffff;
  }
  * { margin: 0; padding: 0; box-sizing: border-box; }
  html, body {
    width: 1200px;
    height: 906px;
    overflow: hidden;
    background: var(--backdrop);
  }
  .ad {
    position: absolute;
    left: 0;
    top: 30px;
    width: 1200px;
    height: 846px;
    overflow: hidden;
    font-family: "Ubuntu", sans-serif;
  }
  .ad__photo {
    position: absolute;
    inset: 0;
    background:
      radial-gradient(ellipse 40% 55% at 88% 35%, rgba(184, 52, 79, 0.45), transparent 70%),
      radial-gradient(ellipse 30% 40% at 10% 55%, rgba(184, 52, 79, 0.35), transparent 70%),
      radial-gradient(ellipse 55% 60% at 55% 60%, var(--leaf-pale), transparent 75%),
      linear-gradient(160deg, var(--leaf-mid) 0%, var(--leaf-pale) 45%, var(--leaf-deep) 100%);
  }
  .ad__headline {
    position: absolute;
    left: 111px;
    top: 122px;
    width: 800px;
    color: var(--white);
    font-family: "Ubuntu", sans-serif;
    font-weight: 700;
    font-size: 64px;
    line-height: 61px;
    letter-spacing: -0.5px;
    white-space: nowrap;
  }
  .ad__band {
    position: absolute;
    left: 0;
    top: 649px;
    width: 1200px;
    height: 125px;
    background: var(--band-green);
  }
  .brand {
    position: absolute;
    left: 114px;
    top: 0;
    width: 314px;
    height: 125px;
    background: var(--white);
    display: flex;
    align-items: center;
    justify-content: center;
  }
  .brand__name {
    color: var(--brand-green);
    font-weight: 500;
    font-size: 22px;
    line-height: 26px;
    white-space: nowrap;
  }
  .ad__tagline {
    position: absolute;
    left: 455px;
    top: 30px;
    color: var(--white);
    font-size: 25.5px;
    line-height: 32px;
    white-space: nowrap;
  }
</style>
</head>
<body>
  <div class="ad">
    <div class="ad__photo" role="img" aria-label="Close-up photograph of a pale green succulent rosette with crimson-tipped leaves"></div>

    <h1 class="ad__headline">We believe<br>in growing regionally<br>appropriate plants for<br>Southern California<br>that beatify our<br>natural and urban<br>landscapes.</h1>

    <div class="ad__band">
      <div class="brand">
        <div class="brand__name">Mesa Verde Growers</div>
      </div>
      <p class="ad__tagline">For over 20 years, our owners and staff take pride<br>in providing timely, expert, and honest service.</p>
    </div>
  </div>
</body>
</html>
```